Flyer for spiritual retreat (yoga, meditation, reiki, raw food)

I would like a flyer to promote my upcoming retreat and a matching Facebook banner.

The name of the retreat is "Wavecrest Of Calm" and the tagline is "retreat into you"

The activities in the retreat include daily meditation, ecstatic dance, spiritual development workshops on intuition, energy healing etc and a reiki session is included.

I would like a flyer designed to promote this, something that is editable as I will be running this multiple times and will need to adjust the flyer to add the dates etc each time.

edit: add that here will be fully catered raw food and juices, and that the retreat price includes all accomodation, meals and workshops.

Please contact me if you need further info. Please also visit my website www.marithovland.com and www.facebook.com/tolvanahaven to see my current events and promotions.

Thank you,

Marit

Reason: Hi all, thank you all for your submissions. Apologies as I am traveling and do not have much access to internet and will review your submissions and provide feedback as soon as possible. Kind regards, Marit.

Target Market(s)

People who like meditation, yoga, fans of rowan mabry and jasper vinek, those interested in personal and spiritual development.

Industry/Entity Type

Health And Wellness

Requirements
Must have
• Please put the included reiki session as as added bonus. Something like "BONUS 30 minute reiki healing session" in a little star/banner/something that stands out.
• Please emphasise the "light" part of Wavecrest as I am going for a play on words between in the light and enlightenment.
• Please include placeholder text for place, location, time
• Placeholder for price
• My name (see attached file - can change colour to suit) and website (www.marithovland.com)
Nice to have
• I prefer rounded designs, curves rather than block designs.
Should not have
• Tolvana Haven logo

```html
<!DOCTYPE html>
<html lang="en">
<head>
<meta charset="utf-8">
<title>Wavecrest Of Calm – Retreat Flyer</title>
<link rel="stylesheet" href="https://fonts.googleapis.com/css2?family=Cinzel:wght@400;700&family=Great+Vibes&family=Oswald:wght@500;700&family=Open+Sans:wght@400;700&display=swap">
<style>
  :root {
    --forest-dark: #1f2a17;
    --forest-mid: #4c5a2e;
    --sunlight: #e9c66a;
    --gold: #f2c230;
    --white: #ffffff;
    --paper: #f7f6f2;
    --list-grey: #8d8d8d;
    --watermark: #e4e1dc;
    --body-text: #4a4a4a;
    --band-brown: #4a3626;
    --bonus-red: #d7191c;
  }
  * { margin: 0; padding: 0; box-sizing: border-box; }
  html, body { width: 857px; height: 1200px; overflow: hidden; background: var(--paper); }
  .flyer { position: relative; width: 857px; height: 1200px; overflow: hidden; background: var(--paper); font-family: "Open Sans", sans-serif; }

  .hero-photo {
    position: absolute; left: 0; top: 0; width: 857px; height: 600px;
    background:
      radial-gradient(ellipse 320px 260px at 720px 120px, rgba(245,214,130,.85), rgba(245,214,130,0) 70%),
      radial-gradient(ellipse 260px 200px at 200px 420px, rgba(90,70,50,.7), rgba(90,70,50,0) 70%),
      linear-gradient(160deg, #2c3a1d 0%, #5b6a35 40%, #8a7b45 70%, #3a3020 100%);
  }

  .title-block { position: absolute; top: 42px; left: 0; width: 100%; text-align: center; color: var(--white); }
  .retreat-name { font-family: "Cinzel", serif; font-weight: 700; font-size: 62px; letter-spacing: 1px; text-shadow: 0 2px 6px rgba(0,0,0,.45); }
  .retreat-name .crest { color: var(--gold); }
  .tagline { font-family: "Cinzel", serif; font-size: 26px; letter-spacing: 8px; text-transform: uppercase; margin-top: 2px; text-shadow: 0 1px 4px rgba(0,0,0,.5); }

  .host-signature { position: absolute; top: 230px; left: 500px; font-family: "Great Vibes", cursive; font-size: 64px; color: var(--white); text-shadow: 0 2px 5px rgba(0,0,0,.4); }

  .content-curve { position: absolute; left: 0; top: 470px; width: 857px; height: 160px; }

  .bonus-badge {
    position: absolute; left: 650px; top: 380px; width: 205px; height: 150px;
    background: var(--bonus-red); border-radius: 22px; transform: rotate(-8deg);
    color: var(--white); text-align: center; padding-top: 14px;
    box-shadow: 0 3px 8px rgba(0,0,0,.3);
  }
  .bonus-duration { display: inline-block; background: var(--white); color: var(--bonus-red); font-family: "Oswald", sans-serif; font-weight: 700; font-size: 26px; padding: 0 10px; border-radius: 6px; line-height: 34px; }
  .bonus-word { font-family: "Oswald", sans-serif; font-weight: 700; font-size: 50px; line-height: 56px; }
  .bonus-detail { font-family: "Oswald", sans-serif; font-weight: 500; font-size: 17px; line-height: 20px; letter-spacing: 1px; }

  .host-watermark { position: absolute; top: 660px; left: 0; width: 100%; text-align: center; font-family: "Great Vibes", cursive; font-size: 150px; color: var(--watermark); }

  .activity-list { position: absolute; top: 620px; left: 0; width: 100%; text-align: center; list-style: none; }
  .activity-list li { font-family: "Cinzel", serif; font-size: 42px; letter-spacing: 4px; line-height: 48px; color: var(--list-grey); }

  .activity-summary { position: absolute; top: 840px; left: 85px; width: 690px; font-size: 21px; line-height: 30px; color: var(--body-text); }

  .event-details { position: absolute; top: 990px; left: 85px; font-size: 22px; color: var(--body-text); }
  .event-details b { font-family: "Oswald", sans-serif; font-weight: 700; margin-right: 10px; letter-spacing: 1px; }
  .event-details span { margin-right: 28px; }

  .footer-band { position: absolute; left: 0; top: 1040px; width: 857px; height: 160px; }
  .footer-text { position: absolute; top: 1080px; left: 0; width: 100%; text-align: center; }
  .website { font-family: "Oswald", sans-serif; font-weight: 700; font-size: 36px; letter-spacing: 2px; color: var(--white); }
  .price-note { font-size: 20px; color: var(--gold); margin-top: 12px; }
</style>
</head>
<body>
<main class="flyer">
  <div class="hero-photo" role="img" aria-label="Photo of a woman sitting on a stone wall in a sunlit forest"></div>

  <header class="title-block">
    <h1 class="retreat-name">Wave<span class="crest">crest</span> Of Calm</h1>
    <p class="tagline">Retreat into you</p>
  </header>

  <p class="host-signature">Marit Hovland</p>

  <svg class="content-curve" viewBox="0 0 857 160" preserveAspectRatio="none" aria-hidden="true">
    <path d="M0 40 C 250 150, 550 60, 857 110 L857 160 L0 160 Z" fill="#ffffff" opacity=".55"/>
    <path d="M0 80 C 260 160, 560 90, 857 130 L857 160 L0 160 Z" fill="var(--paper)"/>
  </svg>

  <div class="bonus-badge">
    <span class="bonus-duration">30minute</span>
    <div class="bonus-word">BONUS</div>
    <div class="bonus-detail">REIKI HEALING SESSION</div>
  </div>

  <p class="host-watermark" aria-hidden="true">Marit Hovland</p>

  <ul class="activity-list">
    <li>Yoga</li>
    <li>Meditation</li>
    <li>Reiki</li>
    <li>Raw Food</li>
  </ul>

  <p class="activity-summary">The activities include, Daily Meditation, Ecstatic Dance, Spiritual Development Workshops on Intuition, Energy Healing etc and a Reiki Session, Catered Raw Food &amp; Juices,</p>

  <p class="event-details">
    <b>DATE</b><span>12 january 2017</span>
    <b>TIME</b><span>10:30am</span>
    <b>PRICE</b><span>A$200</span>
  </p>

  <svg class="footer-band" viewBox="0 0 857 160" preserveAspectRatio="none" aria-hidden="true">
    <path d="M0 20 C 300 -10, 560 10, 857 30 L857 160 L0 160 Z" fill="var(--band-brown)"/>
  </svg>

  <footer class="footer-text">
    <p class="website">www.marithovland.com</p>
    <p class="price-note">The retreat price includes all accomodation, meals and workshops.</p>
  </footer>
</main>
</body>
</html>
```